New Patient Pamphlet

We need a pamphlet designed to attract new patients to our clinic.. We would like it to mention the different types of languages that are spoken at the clinic as well as it being a new patient promotional pack for $195 for exam, clean, fluoride and x-rays. The languages spoken at the clinic are: English, Hindi, Punjabi and Persian.
Please see link below to website so you are able to also add the our services that we provide on the pamphlet that are listed on the website.
https://www.corvexdental.com/

```html
<!DOCTYPE html>
<html lang="en">
<head>
<meta charset="utf-8">
<title>Corvex Dental – New Patient Flyer</title>
<link href="https://fonts.googleapis.com/css2?family=Poppins:wght@400;500;600;700;800&display=swap" rel="stylesheet">
<style>
  :root{
    --navy:#1f4597;
    --green:#3cb54a;
    --lime:#8cc63f;
    --ink:#1a1a1a;
    --grey:#444;
    --white:#ffffff;
  }
  *{margin:0;padding:0;box-sizing:border-box}
  html,body{width:894px;height:1200px;overflow:hidden;background:var(--white)}
  body{font-family:"Poppins",sans-serif;color:var(--ink)}
  .flyer{position:relative;width:894px;height:1200px;background:linear-gradient(135deg,#f2f3f5 0%,#fff 30%,#fff 100%);overflow:hidden}

  .brand{position:absolute;left:52px;top:52px;width:320px}
  .brand-name{display:flex;align-items:center;gap:10px;font-size:34px;font-weight:600;color:var(--navy);line-height:1}
  .brand-dot{width:16px;height:16px;border-radius:50%;background:var(--green)}
  .brand-rule{height:1px;background:#9aa;margin:12px 0 6px}
  .brand-tagline{font-size:12.5px;letter-spacing:6px;color:var(--green);font-weight:500}

  .headline{position:absolute;left:51px;top:180px;font-size:37px;line-height:43px;font-weight:700;color:var(--navy);letter-spacing:-.5px}
  .headline .accent{display:block;color:var(--green);font-weight:500}
  .headline-rule{position:absolute;left:52px;top:333px;width:345px;height:2px;background:#666}
  .intro{position:absolute;left:51px;top:340px;font-size:20px;line-height:28px;color:var(--ink)}
  .intro strong{font-weight:700}

  .offer{position:absolute;left:51px;top:455px;width:276px;height:148px;border:1.5px dotted var(--lime);border-top:none}
  .offer-price{position:absolute;left:-1px;top:0;width:236px;height:74px;background:var(--green);color:var(--white);font-size:54px;font-weight:700;line-height:74px;padding-left:16px;letter-spacing:-1px;clip-path:polygon(0 0,86% 0,100% 100%,0 100%)}
  .offer-price::after{content:"";position:absolute}
  .offer-tab{position:absolute;left:180px;top:0;width:56px;height:74px;background:var(--lime);clip-path:polygon(0 0,60% 0,100% 100%,40% 100%)}
  .offer-text{position:absolute;left:18px;top:84px;font-size:22px;line-height:29px;color:var(--navy);font-weight:500}

  .hero-photo{position:absolute;left:436px;top:20px;width:458px;height:535px;border-radius:40px 0 0 60px;background:radial-gradient(ellipse at 55% 45%,#e8c9a8 0%,#9fb2cc 45%,#eef0f3 80%)}
  .hero-note{position:absolute;left:452px;top:567px;width:400px;text-align:center;font-size:13.5px;line-height:21px;color:var(--grey)}

  .services-icons{position:absolute;left:0;top:640px;width:894px}
  .service{position:absolute;width:150px;text-align:center;transform:translateX(-50%)}
  .service-badge{width:78px;height:78px;margin:0 auto;border-radius:50%;border:3px solid var(--navy);border-top-color:#cfe9c3;border-left-color:#cfe9c3;display:flex;align-items:center;justify-content:center}
  .service-badge span{width:66px;height:66px;border-radius:50%;background:var(--lime);display:flex;align-items:center;justify-content:center;color:var(--white);font-size:36px;font-weight:600}
  .service-label{margin-top:8px;font-size:17px;line-height:21px;color:var(--navy)}

  .treatment-band{position:absolute;left:0;top:855px;width:894px;height:186px;background:var(--navy)}
  .treatment-photo{position:absolute;top:806px;width:177px;height:112px;border:2px solid var(--green);border-radius:8px;box-shadow:0 3px 6px rgba(0,0,0,.25)}
  .treatment-list{position:absolute;left:0;width:894px;display:flex;justify-content:center;align-items:center;gap:5px;font-size:16.2px;font-weight:700;color:var(--white);letter-spacing:-.3px;white-space:nowrap}
  .treatment-list i{width:7px;height:7px;border-radius:50%;background:var(--green);display:inline-block}

  .language-band{position:absolute;left:0;top:1041px;width:894px;height:35px;background:var(--lime);text-align:center;font-size:16px;line-height:35px;color:var(--ink)}

  .contact-call{position:absolute;left:53px;top:1092px}
  .contact-call p{font-size:18px;color:var(--ink)}
  .contact-phone{display:flex;align-items:center;gap:8px;font-size:31px;font-weight:700;color:var(--navy);line-height:40px}
  .contact-address{position:absolute;left:403px;top:1112px;font-size:13.5px;line-height:21px;display:flex;gap:6px}
  .contact-divider{position:absolute;left:601px;top:1108px;width:1px;height:48px;background:#bbb}
  .contact-online{position:absolute;left:619px;top:1112px;font-size:15px;line-height:21px}
  .contact-online div{display:flex;align-items:center;gap:8px}
  .contact-online b{font-weight:700}
</style>
</head>
<body>
<main class="flyer">
  <header class="brand">
    <div class="brand-name"><span class="brand-dot"></span>Corvex Dental</div>
    <div class="brand-rule"></div>
    <div class="brand-tagline">FAMILY DENTAL CARE</div>
  </header>

  <h1 class="headline">GET A BEAUTIFUL,<br>HEALTHY SMILE<span class="accent">AT CORVEX DENTAL</span></h1>
  <div class="headline-rule"></div>
  <p class="intro">At Corvex Dental we provide<br>high-quality, <strong>affordable dental<br>care</strong> for you and your family.</p>

  <section class="offer">
    <div class="offer-tab"></div>
    <div class="offer-price">$195</div>
    <p class="offer-text">for Exam, Clean,<br>Fluoride and X-rays.</p>
  </section>

  <div class="hero-photo" role="img" aria-label="Smiling young family of three sitting together on the floor"></div>
  <p class="hero-note">If you’re looking to achieve a healthier smile at an affordable price, you’ve come to the right place!</p>

  <section class="services-icons">
    <div class="service" style="left:124px">
      <div class="service-badge"><span><svg width="34" height="38" viewBox="0 0 34 38"><path d="M17 2 L31 7 V18 C31 28 24 34 17 36 C10 34 3 28 3 18 V7 Z" fill="none" stroke="#fff" stroke-width="2.5"/><path d="M11 14 C11 11 14 11 17 12.5 C20 11 23 11 23 14 C23 18 21 20 20.5 27 C19.5 27 19 22 17 22 C15 22 14.5 27 13.5 27 C13 20 11 18 11 14Z" fill="#fff"/></svg></span></div>
      <div class="service-label">General<br>Dentistry</div>
    </div>
    <div class="service" style="left:282px">
      <div class="service-badge"><span><svg width="44" height="22" viewBox="0 0 44 22"><path d="M2 6 C12 0 18 4 22 3 C26 4 32 0 42 6 C36 18 28 20 22 20 C16 20 8 18 2 6Z" fill="#fff"/><path d="M6 8 C16 12 28 12 38 8" stroke="#8cc63f" stroke-width="2.5" fill="none"/></svg></span></div>
      <div class="service-label">Cosmetic<br>Dentistry</div>
    </div>
    <div class="service" style="left:441px">
      <div class="service-badge"><span>$</span></div>
      <div class="service-label">Payment<br>Plans</div>
    </div>
    <div class="service" style="left:599px">
      <div class="service-badge"><span><svg width="34" height="36" viewBox="0 0 34 36"><path d="M5 9 C5 3 11 2 17 5 C23 2 29 3 29 9 C29 17 25 20 24 33 C22 33 21 24 17 24 C13 24 12 33 10 33 C9 20 5 17 5 9Z" fill="none" stroke="#fff" stroke-width="2.2"/><rect x="11" y="11" width="12" height="6" rx="1" fill="none" stroke="#fff" stroke-width="2"/><line x1="4" y1="14" x2="30" y2="14" stroke="#fff" stroke-width="2"/></svg></span></div>
      <div class="service-label">Teeth<br>Straightening</div>
    </div>
    <div class="service" style="left:757px">
      <div class="service-badge"><span><svg width="34" height="36" viewBox="0 0 34 36"><path d="M5 9 C5 3 11 2 17 5 C23 2 29 3 29 9 C29 17 25 20 24 33 C22 33 21 24 17 24 C13 24 12 33 10 33 C9 20 5 17 5 9Z" fill="none" stroke="#fff" stroke-width="2.2"/><path d="M20 10 L21 13 L24 14 L21 15 L20 18 L19 15 L16 14 L19 13Z" fill="#fff"/></svg></span></div>
      <div class="service-label">Teeth<br>Whitening</div>
    </div>
  </section>

  <div class="treatment-band"></div>
  <div class="treatment-photo" style="left:54px;background:linear-gradient(135deg,#d9a07f,#f1e2d6 60%,#c98a70)" role="img" aria-label="Dental check-up of a patient's open mouth"></div>
  <div class="treatment-photo" style="left:258px;background:linear-gradient(135deg,#eef1f5,#b7c9e0 55%,#5f86c2)" role="img" aria-label="Dental handpiece beside an x-ray film"></div>
  <div class="treatment-photo" style="left:461px;background:linear-gradient(135deg,#3b3f4a,#d9b49c 50%,#4f7fd6)" role="img" aria-label="Woman fitting a clear teeth aligner"></div>
  <div class="treatment-photo" style="left:665px;background:linear-gradient(180deg,#f7f3ee,#f0c7c7 55%,#efe6d4)" role="img" aria-label="Cross-section of teeth during root canal treatment"></div>

  <div class="treatment-list" style="top:949px">TOOTH REPLACEMENT <i></i> GUM TREATMENT <i></i> IMPLANTS <i></i> ROOT CANAL TREATMENT</div>
  <div class="treatment-list" style="top:978px">PORCELAIN CROWNS <i></i> DENTURES <i></i> LASER-ASISTED TREATMENT <i></i> SEDATION</div>

  <div class="language-band">The languages spoken at the clinic are: English, Hindi, Punjabi and Persian.</div>

  <footer>
    <div class="contact-call">
      <p>Make an Appointment Today</p>
      <div class="contact-phone">
        <svg width="30" height="30" viewBox="0 0 30 30"><circle cx="15" cy="15" r="15" fill="#3cb54a"/><path d="M10 8 L13 8 L14 12 L12 13.5 C13 16 14 17 16.5 18 L18 16 L22 17 L22 20 C22 21 21 22 20 22 C14 22 8 16 8 10 C8 9 9 8 10 8Z" fill="#fff"/></svg>
        (03) 5550 1872
      </div>
    </div>
    <div class="contact-address">
      <svg width="13" height="17" viewBox="0 0 13 17"><path d="M6.5 0 C10 0 13 2.7 13 6.3 C13 10.5 6.5 17 6.5 17 C6.5 17 0 10.5 0 6.3 C0 2.7 3 0 6.5 0Z" fill="#1f4597"/><circle cx="6.5" cy="6.3" r="2.4" fill="#fff"/></svg>
      <div>Corvex Dental,<br>14 Hollis St., Brenmoor,</div>
    </div>
    <div class="contact-divider"></div>
    <div class="contact-online">
      <div><svg width="13" height="13" viewBox="0 0 13 13"><circle cx="6.5" cy="6.5" r="6.5" fill="#1f4597"/><rect x="3" y="4" width="7" height="5" rx="1" fill="#fff"/></svg>admin@corvexdental.com</div>
      <div><svg width="13" height="13" viewBox="0 0 13 13"><circle cx="6.5" cy="6.5" r="5.5" fill="none" stroke="#1f4597" stroke-width="1.5"/><line x1="1" y1="6.5" x2="12" y2="6.5" stroke="#1f4597" stroke-width="1.2"/><ellipse cx="6.5" cy="6.5" rx="2.3" ry="5.5" fill="none" stroke="#1f4597" stroke-width="1.2"/></svg>www.<b>corvexdental</b>.com</div>
    </div>
  </footer>
</main>
</body>
</html>
```